Business Card, Envelopes,Letterhead for Steadfast Blaze Supply
Business Card, Envelopes,Letterhead
Business Card, Envelopes,Letterhead for Steadfast Blaze Supply -
Creative Brief
Use specific fonts
we are open for ideas
Professional
Mark Haverty
47 Corwin Rd. Larkfield Illinois, 60471
847-319-5726 x214
mark@steadfastblaze.example
www.steadfastblaze.example
Id like to see all of my logos utilized through out this project-We are a fire safety company that specilizes in inspecting, servicing selling and certifiying FIRE EXTINGUISHERS RESTAURANT SUPPRESSION SYSTEMS EXIT AND EMERGENCY LIGHTING FIRE ALARMS FIRE SPRINKLERS we have 2 locations- main office/shop-47 Corwin Road Waukegan, Illinois 60085 satelite office- 2917 South Tillman Ave. Chicago Illinois 60603

```html
<!DOCTYPE html>
<html lang="en">
<head>
<meta charset="utf-8">
<title>Steadfast Blaze Supply – Business Card</title>
<link href="https://fonts.googleapis.com/css2?family=Arimo:ital,wght@0,400;0,700;1,700&display=swap" rel="stylesheet">
<style>
  :root {
    --bg: #e9e6e1;
    --card-white: #ffffff;
    --card-black: #0d0d0d;
    --fire-red: #d7262e;
    --fire-yellow: #f7c51e;
    --fire-orange: #f39a1c;
    --ink: #2a2a2a;
    --ink-light: #ffffff;
  }
  * { box-sizing: border-box; margin: 0; padding: 0; }
  html, body { width: 1200px; height: 756px; overflow: hidden; }
  body {
    background: var(--bg);
    font-family: "Arimo", Arial, sans-serif;
    color: var(--ink);
    position: relative;
  }
  .card {
    position: absolute;
    border-radius: 14px;
    box-shadow: 0 2px 6px rgba(0,0,0,.18);
    overflow: hidden;
  }

  /* Front card with contact details */
  .card--contact {
    left: 43px; top: 216px; width: 528px; height: 341px;
    background: var(--card-white);
    display: flex;
  }
  .contact__brand {
    width: 286px;
    display: flex; flex-direction: column; align-items: center; justify-content: center;
    gap: 14px;
    padding: 0 14px;
    border-right: 4px solid var(--fire-red);
  }
  .contact__brand .brand-dot { width: 80px; height: 80px; }
  .contact__brand .brand-name { font-size: 22px; }
  .contact__info {
    flex: 1;
    background: linear-gradient(180deg, #ffffff 0%, #fde9a6 30%, var(--fire-yellow) 65%, var(--fire-orange) 100%);
    padding: 40px 18px 0 20px;
    font-size: 13px;
  }
  .contact__name {
    font-weight: 700; font-style: italic; font-size: 17px; margin-bottom: 24px;
  }
  .contact__address { margin-bottom: 24px; line-height: 1.35; }
  .contact__list { list-style: none; display: flex; flex-direction: column; gap: 6px; }
  .contact__list li { display: flex; align-items: center; gap: 8px; white-space: nowrap; }
  .contact__list svg { width: 12px; height: 12px; fill: var(--ink); flex: none; }

  /* Brand mark replacement */
  .brand-dot { border-radius: 50%; background: var(--fire-red); flex: none; }
  .brand-name {
    color: var(--fire-red); font-weight: 700; text-transform: uppercase;
    text-align: center; line-height: 1.05; letter-spacing: .5px;
  }

  /* Back card, white */
  .card--services {
    left: 619px; top: 48px; width: 545px; height: 307px;
    background: var(--card-white);
  }
  .services__brand {
    position: absolute; left: 0; right: 0; top: 50px;
    display: flex; align-items: center; justify-content: center; gap: 16px;
  }
  .services__brand .brand-dot { width: 70px; height: 70px; }
  .services__brand .brand-name { font-size: 32px; text-align: left; }
  .services__list {
    position: absolute; left: 30px; right: 30px; top: 182px;
    list-style: none; display: flex; flex-wrap: wrap; justify-content: center;
    column-gap: 16px; row-gap: 8px; font-size: 14px;
  }
  .services__list li { display: flex; align-items: center; gap: 6px; }
  .diamond { width: 8px; height: 8px; transform: rotate(45deg); flex: none; }
  .diamond--red { background: var(--fire-red); }
  .diamond--yellow { background: var(--fire-yellow); }

  /* Back card, black */
  .card--dark {
    left: 619px; top: 403px; width: 545px; height: 307px;
    background: var(--card-black); color: var(--ink-light);
  }
  .dark__brand {
    position: absolute; left: 40px; top: 62px; width: 200px;
    display: flex; flex-direction: column; align-items: center; gap: 14px;
  }
  .dark__brand .brand-dot { width: 110px; height: 110px; }
  .dark__brand .brand-name { font-size: 19px; }
  .dark__list {
    position: absolute; right: 30px; top: 52px;
    list-style: none; display: flex; flex-direction: column; align-items: flex-end;
    gap: 23px; font-size: 13px;
  }
  .dark__list li { display: flex; align-items: center; gap: 12px; }
</style>
</head>
<body>

  <section class="card card--contact">
    <div class="contact__brand">
      <div class="brand-dot"></div>
      <div class="brand-name">Steadfast Blaze<br>Supply</div>
    </div>
    <div class="contact__info">
      <p class="contact__name">Mark Haverty</p>
      <p class="contact__address">47 Corwin Rd. Larkfield Illinois,<br>60471</p>
      <ul class="contact__list">
        <li><svg viewBox="0 0 16 16"><path d="M3 1h3l1.5 4-2 1.2a9 9 0 0 0 4.3 4.3L11 8.5l4 1.5v3a2 2 0 0 1-2 2A12 12 0 0 1 1 3a2 2 0 0 1 2-2z"/></svg>847-319-5726 x214</li>
        <li><svg viewBox="0 0 16 16"><rect x="4" y="0.5" width="8" height="15" rx="1.5"/></svg>773-508-2164</li>
        <li><svg viewBox="0 0 16 16"><rect x="1" y="6" width="14" height="8" rx="1"/><rect x="4" y="1" width="8" height="5"/></svg>847-319-5730</li>
        <li><svg viewBox="0 0 16 16"><path d="M1 3h14v10H1z M1 3l7 6 7-6" fill="none" stroke="currentColor" stroke-width="1.6"/></svg>mark@steadfastblaze.example</li>
        <li><svg viewBox="0 0 16 16"><circle cx="8" cy="8" r="6.5" fill="none" stroke="currentColor" stroke-width="1.6"/><path d="M1.5 8h13M8 1.5c-3 3.5-3 9.5 0 13M8 1.5c3 3.5 3 9.5 0 13" fill="none" stroke="currentColor" stroke-width="1.2"/></svg>www.steadfastblaze.example</li>
      </ul>
    </div>
  </section>

  <section class="card card--services">
    <div class="services__brand">
      <div class="brand-dot"></div>
      <div class="brand-name">Steadfast Blaze<br>Supply</div>
    </div>
    <ul class="services__list">
      <li><span class="diamond diamond--red"></span>Fire Extinguishers</li>
      <li><span class="diamond diamond--red"></span>Restaurant Suppression Systems</li>
      <li><span class="diamond diamond--red"></span>Exit And Emergency Lighting</li>
      <li><span class="diamond diamond--red"></span>Fire Alarms</li>
      <li><span class="diamond diamond--red"></span>Fire Sprinklers</li>
    </ul>
  </section>

  <section class="card card--dark">
    <div class="dark__brand">
      <div class="brand-dot"></div>
      <div class="brand-name">Steadfast Blaze Supply</div>
    </div>
    <ul class="dark__list">
      <li>Fire Alarms<span class="diamond diamond--yellow"></span></li>
      <li>Fire Sprinklers<span class="diamond diamond--yellow"></span></li>
      <li>Fire Extinguishers<span class="diamond diamond--yellow"></span></li>
      <li>Exit And Emergency Lighting<span class="diamond diamond--yellow"></span></li>
      <li>Restaurant Suppression Systems<span class="diamond diamond--yellow"></span></li>
    </ul>
  </section>

</body>
</html>
```